BUSINESS CARD MIRELLE KOSVIK

I need a new business card for my personal business.
I am a Naturopath and Nutritionist working doing private consults in the health and wellness arena.
I would like to see designs that are, clean minimalist but colourful.
I like:
White (clean,fresh, minimalist)
pops of one colour ONLY.Choose a colour to run with and keep it simple.
green
light blue
mustard
Bright yellow
Charcoal
The final design should communicate professionalism but also be in touch with nature.
Key Information to include:
MIRELLE KOSVIK
ABN 41 582 307 916
PTRQB 872310
Tel 0491 738 624
NATUROPATH | HERBALIST | NUTRITON CONSULTANT
BHSc (Naturopathic Studies) Grad Dip (Naturopathy)
BACK OF CARD : YOUR NEXT APPOINTMENT ..................................
I already have a logo (picture attached)But I would be more than happy to NOT have this included. I am very Open to cards WITHOUT current logo/ ones that weave the colour of my logo but do not use the logo.
I have included pictures attached to give examples of the styles/colors I enjoy.
Updates
I have added a picture of a mortar and pestle - one just like this would be lovely to include in your entry.
TIA

```html
<!DOCTYPE html>
<html lang="en">
<head>
<meta charset="utf-8">
<title>Mirelle Kosvik — Business Card</title>
<link rel="stylesheet" href="https://fonts.googleapis.com/css2?family=Advent+Pro:wght@100;200;300&family=Montserrat:wght@600;700&family=Oswald:wght@500&display=swap">
<style>
  :root {
    --backdrop: #0fcdb3;
    --card: #f7f7f5;
    --ink: #1c1c1c;
    --ink-soft: #8a8a8a;
    --ink-faint: #a8a8a8;
    --emboss: #e6e6e3;
  }
  * { box-sizing: border-box; margin: 0; padding: 0; }
  html, body {
    width: 1200px; height: 720px; overflow: hidden;
    background: var(--backdrop);
  }
  .stage { position: relative; width: 1200px; height: 720px; }

  .card {
    position: absolute;
    left: 380px;
    width: 440px; height: 250px;
    background: var(--card);
    box-shadow: 0 2px 4px rgba(0,0,0,0.12);
  }
  .card--back { top: 85px; }
  .card--front { top: 385px; }

  /* Back of card */
  .details {
    position: absolute; left: 36px; top: 34px;
    display: grid; grid-template-columns: 58px auto; row-gap: 4px;
    align-items: baseline;
  }
  .details__label {
    font-family: "Montserrat", sans-serif; font-weight: 700;
    font-size: 7px; letter-spacing: 4px; color: var(--ink);
  }
  .details__value {
    font-family: "Advent Pro", sans-serif; font-weight: 300;
    font-size: 10px; letter-spacing: 7px; color: var(--ink-soft);
  }
  .qualifications {
    position: absolute; left: 36px; top: 96px;
    display: grid; grid-template-columns: 58px auto; row-gap: 1px;
    align-items: baseline;
  }
  .qualifications__degree {
    font-family: "Montserrat", sans-serif; font-weight: 700;
    color: var(--ink-soft); letter-spacing: 3px;
  }
  .qualifications__degree--major { font-size: 12px; }
  .qualifications__degree--minor { font-size: 7px; color: var(--ink); }
  .qualifications__field {
    font-family: "Advent Pro", sans-serif; font-weight: 300;
    font-size: 9px; letter-spacing: 4px; color: var(--ink-soft);
  }
  .appointment__title {
    position: absolute; left: 36px; top: 146px;
    font-family: "Montserrat", sans-serif; font-weight: 700;
    font-size: 9px; letter-spacing: 4px; color: var(--ink);
  }
  .appointment__date {
    position: absolute; left: 250px; top: 164px; width: 150px; height: 12px;
    border-bottom: 2px dotted var(--ink);
  }
  .appointment__slash {
    position: absolute; top: -4px;
    font-family: "Advent Pro", sans-serif; font-weight: 300;
    font-size: 14px; color: var(--ink);
  }
  .appointment__time {
    position: absolute; left: 150px; top: 182px;
    font-family: "Montserrat", sans-serif; font-weight: 600;
    font-size: 6.5px; letter-spacing: 2px; color: var(--ink);
  }
  .appointment__line {
    position: absolute; left: 36px; top: 200px; width: 364px; height: 2px;
    border-bottom: 2px dotted var(--ink);
  }

  /* Front of card */
  .emboss {
    position: absolute; left: 120px; top: 25px; width: 200px; height: 200px;
  }
  .identity {
    position: absolute; left: 0; right: 0; top: 98px; text-align: center;
  }
  .identity__name {
    font-family: "Advent Pro", sans-serif; font-weight: 100;
    font-size: 30px; letter-spacing: 5px; color: var(--ink-faint);
    line-height: 1;
  }
  .identity__roles {
    margin-top: 6px;
    font-family: "Oswald", sans-serif; font-weight: 500;
    font-size: 8.5px; letter-spacing: 1.6px; color: var(--ink);
  }
</style>
</head>
<body>
<main class="stage">

  <section class="card card--back" aria-label="Back of card">
    <div class="details">
      <span class="details__label">ABN</span><span class="details__value">41 582 307 916</span>
      <span class="details__label">PTRQB</span><span class="details__value">872310</span>
      <span class="details__label">TEL</span><span class="details__value">0491 738 624</span>
    </div>
    <div class="qualifications">
      <span class="qualifications__degree qualifications__degree--major">BHSC</span><span class="qualifications__field">(NATUROPATHIC STUDIES)</span>
      <span class="qualifications__degree qualifications__degree--minor">GRAD DIP</span><span class="qualifications__field">(NATUROPATHY)</span>
    </div>
    <h2 class="appointment__title">NEXT APPOINTMENT</h2>
    <div class="appointment__date">
      <span class="appointment__slash" style="left:0">/</span>
      <span class="appointment__slash" style="left:40px">/</span>
      <span class="appointment__slash" style="left:80px">/</span>
    </div>
    <span class="appointment__time">AM/PM</span>
    <div class="appointment__line"></div>
  </section>

  <section class="card card--front" aria-label="Front of card">
    <svg class="emboss" viewBox="0 0 200 200" aria-hidden="true">
      <circle cx="100" cy="100" r="98" fill="none" stroke="var(--emboss)" stroke-width="1.5"/>
    </svg>
    <div class="identity">
      <h1 class="identity__name">MIRELLE KOSVIK</h1>
      <p class="identity__roles">NATUROPATH | HERBALIST | NUTRITON CONSULTANT</p>
    </div>
  </section>

</main>
</body>
</html>
```